School Canteen Menu

We operate 30 school canteen/cafes across Melbourne. We are looking to update our old menu to a new attractive design.
We offer a variety of both food and drink and we need to highlight our healthy options. We would like to have a background picture of either salads or healthy sandwiche etc.
We have borken our current menu in catogories according to hot food, cold bar, drinks, ice creams etc.
We would prefer it to be a A4 design but other ideas are welcome.

In summary we need a vibrant attractive applealing design.
My business card with our lgo is also attached
Regards

Tam
Updates

We have two types of menu a secondary menu for students 12-18 and a primary school menu 5-12 year olds. I have attached samples of both.

Reason: Extended deadline as the director of business is away till sunday

Target Market(s)

12 year old to 18 year olds. School Students. As well as Teachers. Prehaps encouraging Teaches with our Freshly made salads will be a feature.

Industry/Entity Type

School

Requirements
Must have
• Viabrant Colors. Greens, Purples, Yellows.
Should not have
• Red Colors. Considered to be a unhealthy color.

```html
<!DOCTYPE html>
<html lang="en">
<head>
<meta charset="utf-8">
<title>Canteen Menu 2012</title>
<link href="https://fonts.googleapis.com/css2?family=Arimo:ital,wght@0,400;0,700;1,700&family=Carlito:wght@400;700&display=swap" rel="stylesheet">
<style>
:root{
  --frame:#9d44ee;
  --sky:#3fcdf4;
  --navy:#12268a;
  --ink:#1b1b1b;
  --rule:#333;
  --pill:#e9f4ff;
  --banner:#0c0c0c;
  --banner-text:#ffff3a;
  --green-mark:#3a9a2a;
}
*{box-sizing:border-box;margin:0;padding:0}
html,body{width:847px;height:1200px;overflow:hidden;background:var(--frame)}
.canvas{position:relative;width:847px;height:1200px;background:var(--frame);font-family:"Carlito",Calibri,sans-serif;color:var(--ink)}
.abs{position:absolute}

/* pyramid poster */
.poster{left:41px;top:34px;width:765px;height:414px;background:var(--sky)}
.title-art{left:96px;top:38px;width:633px;height:58px;border-radius:8px;background:linear-gradient(90deg,#7fd04a,#f28c28,#4aa0e0,#8e5bd0,#f4c430);opacity:.85}
.side-art{border-radius:50%}
.art-left{left:58px;top:168px;width:84px;height:80px;background:#5fb84a}
.art-tr{left:697px;top:104px;width:64px;height:66px;background:#f07a3c}
.art-r{left:728px;top:204px;width:58px;height:62px;background:#f5a13a}
.water{left:103px;top:108px;font:italic 700 15px/1.05 "Arimo",Arial,sans-serif;color:var(--navy)}
.pyramid{left:88px;top:104px}
.tier-label{font:italic 700 12.5px/1.12 "Arimo",Arial,sans-serif;color:var(--navy);text-transform:uppercase}
.badge{width:58px;height:48px}
.badge text{font:italic 700 30px "Arimo",Arial,sans-serif;fill:#fff}
.pill{border:2px solid #2a6fd0;border-radius:12px;background:var(--pill);font:italic 700 7.6px/1.25 "Arimo",Arial,sans-serif;color:var(--navy);display:flex;align-items:center;padding:0 12px}
.pill.note{border-radius:6px;padding:2px 8px;font-size:7px}

/* menu area */
.menu{left:41px;top:448px;width:765px;height:707px;background:linear-gradient(160deg,#eef5e2,#f8f6ef 40%,#eef3e6 70%,#f4efe6)}
.menu-title{left:161px;top:460px;font-size:27px;font-weight:400;color:#222}
.col h2{font-size:17px;font-weight:700;color:#111;height:22px;border-bottom:1.4px solid var(--rule);margin-bottom:1px}
.row{display:flex;align-items:center;min-height:16.8px;border-bottom:1px solid var(--rule);font-size:9.6px;line-height:1.15;padding:1px 0}
.row .tag{width:62px;font-weight:700;padding-left:4px}
.row .item{flex:1;padding-left:3px}
.row .price{width:42px}
.indent .item{padding-left:88px}
.row .note{font-size:7px;width:70px}
.hot .row.tall{min-height:33px}
.salad .row.tall{min-height:25px}
.snacks .row.tall{min-height:29px}
.sub{font-size:9.4px;line-height:1.2;padding:4px 0 2px;border-bottom:1px solid var(--rule)}
.sub small{font-size:8px}
.blank{min-height:16.8px}
.gap{border-bottom:1px solid var(--rule)}
.legend{font-size:9.4px;line-height:1.35}
.green{display:inline-block;width:6px;height:6px;border-radius:50%;background:var(--green-mark);margin-left:4px;vertical-align:1px}
.legend .green{margin:0 4px 0 0}

.hot{left:52px;top:510px;width:208px}
.salad{left:290px;top:510px;width:266px}
.snacks{left:586px;top:510px;width:202px}

.banner{left:47px;top:1108px;width:739px;height:29px;background:var(--banner);color:var(--banner-text);font:700 27px/29px "Arimo",Arial,sans-serif;text-align:center;letter-spacing:.6px}
</style>
</head>
<body>
<div class="canvas">

  <section class="abs poster"></section>
  <div class="abs title-art" role="img" aria-label="Hand lettered title 'The Food Pyramid' formed from fruit and vegetables"></div>
  <div class="abs side-art art-left" role="img" aria-label="Cartoon broccoli character running"></div>
  <div class="abs side-art art-tr" role="img" aria-label="Cartoon tomato character skipping"></div>
  <div class="abs side-art art-r" role="img" aria-label="Cartoon orange character dancing"></div>

  <p class="abs water">DRINK PLENTY<br>OF WATER</p>

  <svg class="abs pyramid" width="430" height="292" viewBox="0 0 430 292" role="img" aria-label="Illustrated food pyramid with breads at the base, fruit and vegetables, dairy, meats and treats at the top">
    <defs>
      <linearGradient id="pyr" x1="0" y1="0" x2="0" y2="1">
        <stop offset="0" stop-color="#f6d24a"/>
        <stop offset=".45" stop-color="#9ee04a"/>
        <stop offset="1" stop-color="#f0b860"/>
      </linearGradient>
    </defs>
    <polygon points="212,4 422,290 4,290" fill="url(#pyr)"/>
  </svg>

  <svg class="abs badge" style="left:362px;top:118px" viewBox="0 0 58 48"><polygon points="0,0 58,24 0,48" fill="var(--navy)"/><text x="4" y="28" style="font-size:6px">SPARINGLY</text></svg>
  <p class="abs tier-label" style="left:428px;top:136px">Very small amounts</p>

  <svg class="abs badge" style="left:404px;top:174px" viewBox="0 0 58 48"><polygon points="0,0 58,24 0,48" fill="var(--navy)"/><text x="6" y="36">2</text></svg>
  <p class="abs tier-label" style="left:467px;top:184px">Meat, chicken, peas, beans<br>fish, &amp; alternatives</p>

  <svg class="abs badge" style="left:446px;top:232px" viewBox="0 0 58 48"><polygon points="0,0 58,24 0,48" fill="var(--navy)"/><text x="6" y="36">3</text></svg>
  <p class="abs tier-label" style="left:513px;top:241px">Milk, cheese<br>&amp; yogurt</p>

  <svg class="abs badge" style="left:486px;top:286px" viewBox="0 0 58 48"><polygon points="0,0 58,24 0,48" fill="var(--navy)"/><text x="6" y="36">5</text></svg>
  <p class="abs tier-label" style="left:551px;top:295px">Fruit, fruit juice<br>&amp; vegetables</p>

  <svg class="abs badge" style="left:524px;top:342px" viewBox="0 0 58 48"><polygon points="0,0 58,24 0,48" fill="var(--navy)"/><text x="4" y="36">6+</text></svg>
  <p class="abs tier-label" style="left:589px;top:343px">Bread, cereals<br>potatoes, rice<br>&amp; pasta</p>

  <p class="abs pill" style="left:96px;top:401px;width:399px;height:20px">Food Pyramid servings above are suitable for children from 5 years of age.</p>
  <p class="abs pill" style="left:96px;top:425px;width:399px;height:21px">Children should do at least 1 hour of moderate intensity activity, most days of the week</p>
  <p class="abs pill note" style="left:517px;top:404px;width:216px;height:38px">For younger children, start with smaller and fewer servings and increase up to the guidelines recommended, according to the child's own growth and appetite.</p>

  <div class="abs menu" role="img" aria-label="Soft faded background photograph of fresh salads and healthy sandwiches"></div>
  <h1 class="abs menu-title">Canteen Menu 2012</h1>

  <section class="abs col hot">
    <h2>Hot Food</h2>
    <div class="row"><span class="tag">Jaffles</span><span class="item">Cheese</span><span class="price">$2.50</span></div>
    <div class="row"><span class="tag"></span><span class="item">Spaghetti<i class="green"></i></span><span class="price">$2.50</span></div>
    <div class="row"><span class="tag"></span><span class="item">Baked Beans<i class="green"></i></span><span class="price">$2.50</span></div>
    <div class="row"><span class="tag"></span><span class="item">Ham &amp; Cheese</span><span class="price">$2.60</span></div>
    <div class="row" style="min-height:27px"><span class="tag"></span><span class="item">Ham, Cheese &amp;<br>Pineapple</span><span class="price">$3.00</span></div>
    <div class="row"><span class="item">Lasagne 97% Fat Free<i class="green"></i></span><span class="price">$3.60</span></div>
    <div class="row"><span class="item">Macaroni &amp; Cheese 97% Fat Free<i class="green"></i></span><span class="price">$3.60</span></div>
    <div class="row"><span class="item">Meat Pie</span><span class="price">$3.20</span></div>
    <div class="row"><span class="item">Party Pie or Party Sausage Roll</span><span class="price">$1.00</span></div>
    <div class="row"><span class="item">Sausage Roll</span><span class="price">$3.00</span></div>
    <div class="gap" style="height:14px"></div>
    <div class="row tall"><span class="item">Flame Grilled Beef Burger<i class="green"></i><br>with lettuce, cheese and tomato</span><span class="price">$4.00</span></div>
    <div class="row tall"><span class="item">Chicken Burger<br>with lettuce, cheese &amp; mayonnaise</span><span class="price">$4.00</span></div>
    <div class="row tall"><span class="item">Baked Chicken Schnitzel Roll<br>with lettuce, cheese, tomato &amp; mayo</span><span class="price">$4.20</span></div>
    <div class="row"><span class="item">Corn Cobette<i class="green"></i></span><span class="price">$1.20</span></div>
    <div class="row"><span class="item">Noodles - Chicken or Beef</span><span class="price">$2.60</span></div>
    <div class="row tall"><span class="item">Chicken Nuggets 80c<br>each &nbsp;&nbsp;&nbsp;&nbsp;&nbsp;&nbsp;&nbsp;&nbsp;&nbsp;&nbsp;&nbsp;&nbsp;&nbsp;&nbsp;&nbsp;&nbsp;(3)</span><span class="price">$2.20</span></div>
    <div class="row"><span class="item">Steamed Dim Sim</span><span class="price">$0.90</span></div>
    <div class="row"><span class="item">Hot Dog</span><span class="price">$3.00</span></div>
    <div class="gap" style="height:26px"></div>
    <h2 style="margin-top:18px">Specials</h2>
    <div class="row" style="border-bottom:none"><span class="item"><b>Health Pack 1</b></span><span class="price">$6.00</span></div>
    <div class="row" style="min-height:27px"><span class="item">Salad Roll, Cookie &amp; 200ml Fruit Box<br>$5.00</span></div>
    <div class="row" style="border-bottom:none"><span class="item"><b>Health Pack 2</b></span><span class="price">$6.00</span></div>
    <div class="row" style="min-height:27px"><span class="item">Any 97% Fat Free Pasta,300ml FlavouredMilk<br>(FRESH)</span></div>
  </section>

  <section class="abs col salad">
    <h2>Salad Plates</h2>
    <div class="sub"><b>Salad Plates</b><br><small>all with lettuce, cucumber, carrot, tomato &amp; beetroot</small></div>
    <div class="row indent" style="margin-top:6px;border-top:1px solid var(--rule)"><span class="item">Salad<i class="green"></i></span><span class="price">$3.40</span></div>
    <div class="row indent"><span class="item">Egg<i class="green"></i></span><span class="price">$3.60</span></div>
    <div class="row indent tall"><span class="item">Chicken<i class="green"></i></span><span class="price">$3.90</span></div>
    <div class="row indent"><span class="item">Cheese</span><span class="price">$3.60</span></div>
    <div class="row indent"><span class="item">Ham<i class="green"></i></span><span class="price">$3.60</span></div>
    <div class="row indent"><span class="item">Tuna<i class="green"></i></span><span class="price">$3.60</span></div>
    <h2 style="margin-top:30px">Sandwiches</h2>
    <div class="sub"><b>Sandwiches</b><br><b>Rolls</b> <small>60c extra</small></div>
    <div class="row indent tall" style="margin-top:10px;border-top:1px solid var(--rule)"><span class="item">Salad<i class="green"></i></span><span class="note">lettuce, tomato, carrot, beetroot, cucumber</span><span class="price">$2.80</span></div>
    <div class="row indent"><span class="item">Ham &amp; Tomato<i class="green"></i></span><span class="price">$2.40</span></div>
    <div class="row indent tall"><span class="item">Ham, Cheese &amp; Tomato<i class="green"></i></span><span class="price">$2.60</span></div>
    <div class="row indent"><span class="item">Cheese &amp; Tomato<i class="green"></i></span><span class="price">$2.40</span></div>
    <div class="row indent"><span class="item">Cheese &amp; Salad<i class="green"></i></span><span class="price">$3.00</span></div>
    <div class="row indent tall"><span class="item">Egg &amp; Lettuce<i class="green"></i></span><span class="price">$2.80</span></div>
    <div class="row indent"><span class="item">Chicken &amp; Salad<i class="green"></i></span><span class="price">$3.10</span></div>
    <div class="row indent"><span class="item">Tuna &amp; Tomato<i class="green"></i></span><span class="price">$2.90</span></div>
    <div class="row indent"><span class="item">Tuna, Lettuce &amp; Mayonnaise</span><span class="price">$3.00</span></div>
    <div class="row indent"><span class="item">Yeast Spread</span><span class="price">$1.60</span></div>
    <div class="row indent"><span class="item">Ham</span><span class="price">$2.20</span></div>
    <div class="row"><span class="item">extra fillings</span><span class="price">$0.40</span></div>
    <h2 style="margin-top:16px">Wraps</h2>
    <div class="row" style="margin-top:6px;border-top:1px solid var(--rule)"><span class="item" style="flex:0 0 94px">BBQ Chicken</span><span class="item">Chicken, Lettuce, BBQ Sauce</span><span class="price">$3.60</span></div>
    <div class="row" style="min-height:28px"><span class="item" style="flex:0 0 94px">Sweet Chilli<br>Chicken</span><span class="item">Chicken, Lettuce, Sweet Chilli<br>Sauce</span><span class="price">$3.60</span></div>
  </section>

  <section class="abs col snacks">
    <h2>Snacks</h2>
    <div class="row"><span class="item">Pikelets<i class="green"></i></span><span class="price">$0.80</span></div>
    <div class="row"><span class="item">Pop Corn<i class="green"></i></span><span class="price">$2.00</span></div>
    <div class="row"><span class="item">Fruit Salad – small<i class="green"></i></span><span class="price">$1.50</span></div>
    <div class="row"><span class="item">Fruit of the day<i class="green"></i></span><span class="price">$0.80</span></div>
    <div class="row tall"><span class="item">Jelly Cup with Fruit</span><span class="price">$1.50</span></div>
    <div class="row"><span class="item">Anzac Cookie</span><span class="price">$2.00</span></div>
    <div class="row"><span class="item">Mini Muffins (home baked)</span><span class="price">$0.80</span></div>
    <div class="row blank"></div>
    <div class="row blank" style="min-height:28px"></div>
    <h2 style="margin-top:26px">Drinks</h2>
    <div class="row tall"><span class="item">Flavoured Milk (300ml) Chocolate,<br>Strawberry, Iced Coffee <b>(FRESH)</b></span><span class="price">$2.50</span></div>
    <div class="row"><span class="item">Water (600ml)<i class="green"></i></span><span class="price">$2.30</span></div>
    <div class="row tall"><span class="item">Fruit Juice (200ml) Tropical, Orange,<br>Apple</span><span class="price">$1.50</span></div>
    <h2 style="margin-top:40px">Ice Creams</h2>
    <div class="row"><span class="item">Frozen Orange Wedge<i class="green"></i></span><span class="price">$0.20</span></div>
    <div class="row"><span class="item">Frozen Pineapple Ring<i class="green"></i></span><span class="price">$0.50</span></div>
    <div class="row"><span class="item">Frozen Fruit Yoghurt</span><span class="price">$2.00</span></div>
    <div class="row"><span class="item">Jolly Freeze</span><span class="price">$0.80</span></div>
    <div class="row"><span class="item">Bright Pop_Orange, Lemonade</span><span class="price">$2.00</span></div>
    <div class="row blank" style="min-height:22px"></div>
    <p class="legend" style="margin-top:48px"><i class="green"></i>Foods marked with a green dot are green foods and can be eaten everyday</p>
  </section>

  <p class="abs banner">Canteen Closed on Tuesdays &amp; Wednesdays</p>
</div>
</body>
</html>
```